Flavour Wheel - Illustrator Graph

I need my basic layout, from the sample I provided, turned into a professional looking flavour wheel.

I have attached a sample of a final design I like, but please use your own creativity also.

All the exact words I need are on the uploaded illustration.

I would need the file supplied to me in .ai

Industry/Entity Type

Wheel

Font styles to use
Sans Serif

Colors

Designer to choose colors to be used in the design.

Requirements
Must have
• Files must be supplied in .ai format with fonts not outlined.
• I need each segment separated so I can change the colours if needed myself.
Nice to have
• I like small white gaps between the sections.

```html
<!DOCTYPE html>
<html lang="en">
<head>
<meta charset="utf-8">
<title>Flavour Wheel</title>
<link rel="stylesheet" href="https://fonts.googleapis.com/css2?family=Barlow:wght@400;500;600&display=swap">
<style>
  :root {
    --paper: #ffffff;
    /* taste ramps: deep, mid, light */
    --earthy-1: #7a5230; --earthy-2: #a67c45; --earthy-3: #c9a46a;
    --sweet-1: #b8134f;  --sweet-2: #d2477a;  --sweet-3: #e58aa8;
    --salty-1: #24648a;  --salty-2: #4a8fb5;  --salty-3: #88bcd6;
    --savoury-1: #5e3590; --savoury-2: #8461b4; --savoury-3: #b29ad3;
    --spicy-1: #b8341e;  --spicy-2: #dc6544;  --spicy-3: #ec9a74;
    --smokey-1: #393d44; --smokey-2: #676d76; --smokey-3: #9ea3aa;
    --sour-1: #477e27;   --sour-2: #76aa48;   --sour-3: #a9cf7e;
  }
  html, body { margin: 0; padding: 0; width: 1200px; height: 1200px; overflow: hidden; background: var(--paper); }
  .flavour-wheel { display: block; width: 1200px; height: 1200px; font-family: "Barlow", sans-serif; }
  .ring circle { fill: none; stroke: var(--c); }
  .taste circle { stroke-width: 250; }
  .taste text { fill: #fff; font-size: 27px; font-weight: 500; letter-spacing: 1.5px; text-anchor: middle; dominant-baseline: central; }
  .family circle { stroke-width: 185; }
  .family text { fill: #fff; font-size: 19px; font-weight: 600; letter-spacing: 1px; text-anchor: middle; dominant-baseline: central; }
  .note circle { fill: none; stroke: var(--c); stroke-width: 34; stroke-dasharray: 5.2 360; }
  .note text { fill: var(--ink); font-size: 19.5px; font-weight: 400; dominant-baseline: central; text-anchor: start; }
  .note.left text { text-anchor: end; }
  .gap { stroke: var(--paper); stroke-width: 5; }
  .hub { fill: var(--paper); }
  .earthy-notes { --ink: var(--earthy-1); }
  .sweet-notes { --ink: var(--sweet-1); }
  .salty-notes { --ink: var(--salty-1); }
  .savoury-notes { --ink: var(--savoury-1); }
  .spicy-notes { --ink: var(--spicy-1); }
  .smokey-notes { --ink: var(--smokey-1); }
  .sour-notes { --ink: var(--sour-1); }
</style>
</head>
<body>
<svg class="flavour-wheel" viewBox="0 0 1500 1500" xmlns="http://www.w3.org/2000/svg" role="img" aria-label="Flavour wheel">
  <g transform="translate(742 740)">

    <!-- tastes -->
    <g class="ring taste">
      <g style="--c:var(--earthy-1)" transform="rotate(267)"><circle r="125" pathLength="360" stroke-dasharray="93 360"/><text x="150" transform="rotate(46.5)">EARTHY</text></g>
      <g style="--c:var(--sweet-1)" transform="rotate(0)"><circle r="125" pathLength="360" stroke-dasharray="46 360"/><text x="140" transform="rotate(23)">SWEET</text></g>
      <g style="--c:var(--salty-1)" transform="rotate(46)"><circle r="125" pathLength="360" stroke-dasharray="31 360"/><text x="135" transform="rotate(15.5)">SALTY</text></g>
      <g style="--c:var(--savoury-1)" transform="rotate(77)"><circle r="125" pathLength="360" stroke-dasharray="36 360"/><text x="150" transform="rotate(18)">SAVOURY</text></g>
      <g style="--c:var(--spicy-1)" transform="rotate(113)"><circle r="125" pathLength="360" stroke-dasharray="71.5 360"/><text x="-140" transform="rotate(215.75)">SPICY</text></g>
      <g style="--c:var(--smokey-1)" transform="rotate(184.5)"><circle r="125" pathLength="360" stroke-dasharray="31.5 360"/><text x="-148" transform="rotate(195.75)">SMOKEY</text></g>
      <g style="--c:var(--sour-1)" transform="rotate(216)"><circle r="125" pathLength="360" stroke-dasharray="51 360"/><text x="-135" transform="rotate(205.5)">SOUR</text></g>
    </g>

    <!-- flavour families -->
    <g class="ring family">
      <g style="--c:var(--earthy-2)" transform="rotate(267)"><circle r="347.5" pathLength="360" stroke-dasharray="19 360"/><text x="347" transform="rotate(9.5)">FLORAL</text></g>
      <g style="--c:#8d6536" transform="rotate(-74)"><circle r="347.5" pathLength="360" stroke-dasharray="27 360"/><text x="347" transform="rotate(13.5)">HERBY</text></g>
      <g style="--c:var(--earthy-2)" transform="rotate(-47)"><circle r="347.5" pathLength="360" stroke-dasharray="21 360"/><text x="347" transform="rotate(10.5)">NUTTY</text></g>
      <g style="--c:#8d6536" transform="rotate(-26)"><circle r="347.5" pathLength="360" stroke-dasharray="26 360"/><text x="347" transform="rotate(13)">BUTTERY</text></g>
      <g style="--c:var(--sweet-2)" transform="rotate(0)"><circle r="347.5" pathLength="360" stroke-dasharray="15 360"/><text x="347" transform="rotate(7.5)">FRUITY</text></g>
      <g style="--c:#c52e66" transform="rotate(15)"><circle r="347.5" pathLength="360" stroke-dasharray="16 360"/><text x="347" transform="rotate(8)">SUGARY</text></g>
      <g style="--c:var(--sweet-2)" transform="rotate(31)"><circle r="347.5" pathLength="360" stroke-dasharray="15 360"/><text x="347" transform="rotate(7.5)">CARAMEL</text></g>
      <g style="--c:var(--salty-2)" transform="rotate(46)"><circle r="347.5" pathLength="360" stroke-dasharray="16 360"/><text x="347" transform="rotate(8)">CHARRED</text></g>
      <g style="--c:#377aa0" transform="rotate(62)"><circle r="347.5" pathLength="360" stroke-dasharray="15 360"/><text x="347" transform="rotate(7.5)">BRINY</text></g>
      <g style="--c:var(--savoury-2)" transform="rotate(77)"><circle r="347.5" pathLength="360" stroke-dasharray="15 360"/><text x="347" transform="rotate(7.5)">MEATINESS</text></g>
      <g style="--c:#714aa2" transform="rotate(92)"><circle r="347.5" pathLength="360" stroke-dasharray="21 360"/><text x="347" transform="rotate(10.5)">UMAMI</text></g>
      <g style="--c:var(--spicy-2)" transform="rotate(113)"><circle r="347.5" pathLength="360" stroke-dasharray="25 360"/><text x="-347" transform="rotate(192.5)">CHILLI</text></g>
      <g style="--c:#ca4d31" transform="rotate(138)"><circle r="347.5" pathLength="360" stroke-dasharray="22 360"/><text x="-347" transform="rotate(191)">PEPPERY</text></g>
      <g style="--c:var(--spicy-2)" transform="rotate(160)"><circle r="347.5" pathLength="360" stroke-dasharray="24.5 360"/><text x="-347" transform="rotate(192.25)">CAJUN</text></g>
      <g style="--c:#50555d" transform="rotate(184.5)"><circle r="347.5" pathLength="360" stroke-dasharray="10.5 360"/><text x="-347" transform="rotate(185.25)">WOODY</text></g>
      <g style="--c:var(--smokey-2)" transform="rotate(195)"><circle r="347.5" pathLength="360" stroke-dasharray="10 360"/><text x="-347" transform="rotate(185)">FRUITY</text></g>
      <g style="--c:#50555d" transform="rotate(205)"><circle r="347.5" pathLength="360" stroke-dasharray="11 360"/><text x="-347" transform="rotate(185.5)">ACRID</text></g>
      <g style="--c:var(--sour-2)" transform="rotate(216)"><circle r="347.5" pathLength="360" stroke-dasharray="20 360"/><text x="-347" transform="rotate(190)">BITTER</text></g>
      <g style="--c:#5e9437" transform="rotate(236)"><circle r="347.5" pathLength="360" stroke-dasharray="12 360"/><text x="-347" transform="rotate(186)">BINEGARY</text></g>
      <g style="--c:var(--sour-2)" transform="rotate(248)"><circle r="347.5" pathLength="360" stroke-dasharray="19 360"/><text x="-347" transform="rotate(189.5)">CITRUS</text></g>
    </g>

    <!-- segment gaps -->
    <g class="gaps">
      <line class="gap" x1="0" x2="444" transform="rotate(267)"/>
      <line class="gap" x1="0" x2="444" transform="rotate(0)"/>
      <line class="gap" x1="0" x2="444" transform="rotate(46)"/>
      <line class="gap" x1="0" x2="444" transform="rotate(77)"/>
      <line class="gap" x1="0" x2="444" transform="rotate(113)"/>
      <line class="gap" x1="0" x2="444" transform="rotate(184.5)"/>
      <line class="gap" x1="0" x2="444" transform="rotate(216)"/>
      <line class="gap" x1="250" x2="444" transform="rotate(-74)"/>
      <line class="gap" x1="250" x2="444" transform="rotate(-47)"/>
      <line class="gap" x1="250" x2="444" transform="rotate(-26)"/>
      <line class="gap" x1="250" x2="444" transform="rotate(15)"/>
      <line class="gap" x1="250" x2="444" transform="rotate(31)"/>
      <line class="gap" x1="250" x2="444" transform="rotate(62)"/>
      <line class="gap" x1="250" x2="444" transform="rotate(92)"/>
      <line class="gap" x1="250" x2="444" transform="rotate(138)"/>
      <line class="gap" x1="250" x2="444" transform="rotate(160)"/>
      <line class="gap" x1="250" x2="444" transform="rotate(195)"/>
      <line class="gap" x1="250" x2="444" transform="rotate(205)"/>
      <line class="gap" x1="250" x2="444" transform="rotate(236)"/>
      <line class="gap" x1="250" x2="444" transform="rotate(248)"/>
    </g>

    <circle class="hub" r="54"/>

    <!-- flavour notes -->
    <g class="notes">
      <g class="earthy-notes">
        <g class="note" style="--c:var(--earthy-1)" transform="rotate(-90)"><circle r="464" pathLength="360" transform="rotate(-2.57)"/><text x="498">Coriander</text></g>
        <g class="note" style="--c:var(--earthy-2)" transform="rotate(-84.86)"><circle r="464" pathLength="360" transform="rotate(-2.57)"/><text x="498">Celery</text></g>
        <g class="note" style="--c:var(--earthy-3)" transform="rotate(-79.71)"><circle r="464" pathLength="360" transform="rotate(-2.57)"/><text x="498">Tea</text></g>
        <g class="note" style="--c:var(--earthy-1)" transform="rotate(-74.57)"><circle r="464" pathLength="360" transform="rotate(-2.57)"/><text x="498">Sage</text></g>
        <g class="note" style="--c:var(--earthy-2)" transform="rotate(-69.43)"><circle r="464" pathLength="360" transform="rotate(-2.57)"/><text x="498">Oregano</text></g>
        <g class="note" style="--c:var(--earthy-3)" transform="rotate(-64.29)"><circle r="464" pathLength="360" transform="rotate(-2.57)"/><text x="498">Thyme</text></g>
        <g class="note" style="--c:var(--earthy-1)" transform="rotate(-59.14)"><circle r="464" pathLength="360" transform="rotate(-2.57)"/><text x="498">Rosemary</text></g>
        <g class="note" style="--c:var(--earthy-2)" transform="rotate(-54)"><circle r="464" pathLength="360" transform="rotate(-2.57)"/><text x="498">Bay Leaf</text></g>
        <g class="note" style="--c:var(--earthy-3)" transform="rotate(-48.86)"><circle r="464" pathLength="360" transform="rotate(-2.57)"/><text x="498">Fennel</text></g>
        <g class="note" style="--c:var(--earthy-1)" transform="rotate(-43.71)"><circle r="464" pathLength="360" transform="rotate(-2.57)"/><text x="498">Five Spice</text></g>
        <g class="note" style="--c:var(--earthy-2)" transform="rotate(-38.57)"><circle r="464" pathLength="360" transform="rotate(-2.57)"/><text x="498">Nutmeg</text></g>
        <g class="note" style="--c:var(--earthy-3)" transform="rotate(-33.43)"><circle r="464" pathLength="360" transform="rotate(-2.57)"/><text x="498">Tumeric</text></g>
        <g class="note" style="--c:var(--earthy-1)" transform="rotate(-28.29)"><circle r="464" pathLength="360" transform="rotate(-2.57)"/><text x="498">Star Anise</text></g>
        <g class="note" style="--c:var(--earthy-2)" transform="rotate(-23.14)"><circle r="464" pathLength="360" transform="rotate(-2.57)"/><text x="498">Cinnamon</text></g>
        <g class="note" style="--c:var(--earthy-3)" transform="rotate(-18)"><circle r="464" pathLength="360" transform="rotate(-2.57)"/><text x="498">Clove</text></g>
        <g class="note" style="--c:var(--earthy-1)" transform="rotate(-12.86)"><circle r="464" pathLength="360" transform="rotate(-2.57)"/><text x="498">Pecan</text></g>
        <g class="note" style="--c:var(--earthy-2)" transform="rotate(-7.71)"><circle r="464" pathLength="360" transform="rotate(-2.57)"/><text x="498">Coffee</text></g>
        <g class="note" style="--c:var(--earthy-3)" transform="rotate(-2.57)"><circle r="464" pathLength="360" transform="rotate(-2.57)"/><text x="498">Butter</text></g>
      </g>
      <g class="sweet-notes">
        <g class="note" style="--c:var(--sweet-1)" transform="rotate(2.57)"><circle r="464" pathLength="360" transform="rotate(-2.57)"/><text x="498">Fruit Juice</text></g>
        <g class="note" style="--c:var(--sweet-2)" transform="rotate(7.71)"><circle r="464" pathLength="360" transform="rotate(-2.57)"/><text x="498">Fruits</text></g>
        <g class="note" style="--c:var(--sweet-3)" transform="rotate(12.86)"><circle r="464" pathLength="360" transform="rotate(-2.57)"/><text x="498">Sauce / Ketchup</text></g>
        <g class="note" style="--c:var(--sweet-1)" transform="rotate(18)"><circle r="464" pathLength="360" transform="rotate(-2.57)"/><text x="498">Cola</text></g>
        <g class="note" style="--c:var(--sweet-2)" transform="rotate(23.14)"><circle r="464" pathLength="360" transform="rotate(-2.57)"/><text x="498">Agave Nectar</text></g>
        <g class="note" style="--c:var(--sweet-3)" transform="rotate(28.29)"><circle r="464" pathLength="360" transform="rotate(-2.57)"/><text x="498">Sugars</text></g>
        <g class="note" style="--c:var(--sweet-1)" transform="rotate(33.43)"><circle r="464" pathLength="360" transform="rotate(-2.57)"/><text x="498">Honey</text></g>
        <g class="note" style="--c:var(--sweet-2)" transform="rotate(38.57)"><circle r="464" pathLength="360" transform="rotate(-2.57)"/><text x="498">Molasses</text></g>
        <g class="note" style="--c:var(--sweet-3)" transform="rotate(43.71)"><circle r="464" pathLength="360" transform="rotate(-2.57)"/><text x="498">Maple Syrup</text></g>
      </g>
      <g class="salty-notes">
        <g class="note" style="--c:var(--salty-1)" transform="rotate(48.86)"><circle r="464" pathLength="360" transform="rotate(-2.57)"/><text x="498">Anchovies</text></g>
        <g class="note" style="--c:var(--salty-2)" transform="rotate(54)"><circle r="464" pathLength="360" transform="rotate(-2.57)"/><text x="498">Garlic</text></g>
        <g class="note" style="--c:var(--salty-3)" transform="rotate(59.14)"><circle r="464" pathLength="360" transform="rotate(-2.57)"/><text x="498">Sea Salt</text></g>
        <g class="note" style="--c:var(--salty-1)" transform="rotate(64.29)"><circle r="464" pathLength="360" transform="rotate(-2.57)"/><text x="498">Kosher Salt</text></g>
        <g class="note" style="--c:var(--salty-2)" transform="rotate(69.43)"><circle r="464" pathLength="360" transform="rotate(-2.57)"/><text x="498">Soy Sauce</text></g>
        <g class="note" style="--c:var(--salty-3)" transform="rotate(74.57)"><circle r="464" pathLength="360" transform="rotate(-2.57)"/><text x="498">Fish Sauce</text></g>
      </g>
      <g class="savoury-notes">
        <g class="note" style="--c:var(--savoury-1)" transform="rotate(79.71)"><circle r="464" pathLength="360" transform="rotate(-2.57)"/><text x="498">Worcestershire</text></g>
        <g class="note" style="--c:var(--savoury-2)" transform="rotate(84.86)"><circle r="464" pathLength="360" transform="rotate(-2.57)"/><text x="498">Seasoning Sauce</text></g>
        <g class="note" style="--c:var(--savoury-3)" transform="rotate(90)"><circle r="464" pathLength="360" transform="rotate(-2.57)"/><text x="498">Phosphates</text></g>
        <g class="note" style="--c:var(--savoury-1)" transform="rotate(95.14)"><circle r="464" pathLength="360" transform="rotate(-2.57)"/><text x="498">Stocks</text></g>
        <g class="note" style="--c:var(--savoury-2)" transform="rotate(100.29)"><circle r="464" pathLength="360" transform="rotate(-2.57)"/><text x="498">Lard</text></g>
        <g class="note" style="--c:var(--savoury-3)" transform="rotate(105.43)"><circle r="464" pathLength="360" transform="rotate(-2.57)"/><text x="498">Yeastspread</text></g>
        <g class="note left" style="--c:var(--savoury-1)" transform="rotate(290.57)"><circle r="464" pathLength="360" transform="rotate(177.43)"/><text x="-498">MSG</text></g>
      </g>
      <g class="spicy-notes">
        <g class="note left" style="--c:var(--spicy-1)" transform="rotate(295.71)"><circle r="464" pathLength="360" transform="rotate(177.43)"/><text x="-498">Horseradish</text></g>
        <g class="note left" style="--c:var(--spicy-2)" transform="rotate(300.86)"><circle r="464" pathLength="360" transform="rotate(177.43)"/><text x="-498">Wasabi</text></g>
        <g class="note left" style="--c:var(--spicy-3)" transform="rotate(306)"><circle r="464" pathLength="360" transform="rotate(177.43)"/><text x="-498">Pepper</text></g>
        <g class="note left" style="--c:var(--spicy-1)" transform="rotate(311.14)"><circle r="464" pathLength="360" transform="rotate(177.43)"/><text x="-498">Cumin</text></g>
        <g class="note left" style="--c:var(--spicy-2)" transform="rotate(316.29)"><circle r="464" pathLength="360" transform="rotate(177.43)"/><text x="-498">Allspice</text></g>
        <g class="note left" style="--c:var(--spicy-3)" transform="rotate(321.43)"><circle r="464" pathLength="360" transform="rotate(177.43)"/><text x="-498">Szechuan</text></g>
        <g class="note left" style="--c:var(--spicy-1)" transform="rotate(326.57)"><circle r="464" pathLength="360" transform="rotate(177.43)"/><text x="-498">Onion</text></g>
        <g class="note left" style="--c:var(--spicy-2)" transform="rotate(331.71)"><circle r="464" pathLength="360" transform="rotate(177.43)"/><text x="-498">Chipotle</text></g>
        <g class="note left" style="--c:var(--spicy-3)" transform="rotate(336.86)"><circle r="464" pathLength="360" transform="rotate(177.43)"/><text x="-498">Jalapeno</text></g>
        <g class="note left" style="--c:var(--spicy-1)" transform="rotate(342)"><circle r="464" pathLength="360" transform="rotate(177.43)"/><text x="-498">Hot Sauce</text></g>
        <g class="note left" style="--c:var(--spicy-2)" transform="rotate(347.14)"><circle r="464" pathLength="360" transform="rotate(177.43)"/><text x="-498">Habanero</text></g>
        <g class="note left" style="--c:var(--spicy-3)" transform="rotate(352.29)"><circle r="464" pathLength="360" transform="rotate(177.43)"/><text x="-498">Red Pepper</text></g>
        <g class="note left" style="--c:var(--spicy-1)" transform="rotate(357.43)"><circle r="464" pathLength="360" transform="rotate(177.43)"/><text x="-498">Mustard</text></g>
        <g class="note left" style="--c:var(--spicy-2)" transform="rotate(362.57)"><circle r="464" pathLength="360" transform="rotate(177.43)"/><text x="-498">Paprika</text></g>
      </g>
      <g class="smokey-notes">
        <g class="note left" style="--c:var(--smokey-1)" transform="rotate(367.71)"><circle r="464" pathLength="360" transform="rotate(177.43)"/><text x="-498">Hard woods</text></g>
        <g class="note left" style="--c:var(--smokey-2)" transform="rotate(372.86)"><circle r="464" pathLength="360" transform="rotate(177.43)"/><text x="-498">Fruit woods</text></g>
        <g class="note left" style="--c:var(--smokey-3)" transform="rotate(378)"><circle r="464" pathLength="360" transform="rotate(177.43)"/><text x="-498">Charcoal</text></g>
        <g class="note left" style="--c:var(--smokey-1)" transform="rotate(383.14)"><circle r="464" pathLength="360" transform="rotate(177.43)"/><text x="-498">Whiskey</text></g>
        <g class="note left" style="--c:var(--smokey-2)" transform="rotate(388.29)"><circle r="464" pathLength="360" transform="rotate(177.43)"/><text x="-498">Bourbon</text></g>
        <g class="note left" style="--c:var(--smokey-3)" transform="rotate(393.43)"><circle r="464" pathLength="360" transform="rotate(177.43)"/><text x="-498">Creosote</text></g>
      </g>
      <g class="sour-notes">
        <g class="note left" style="--c:var(--sour-1)" transform="rotate(398.57)"><circle r="464" pathLength="360" transform="rotate(177.43)"/><text x="-498">Cocktail Bitters</text></g>
        <g class="note left" style="--c:var(--sour-2)" transform="rotate(403.71)"><circle r="464" pathLength="360" transform="rotate(177.43)"/><text x="-498">Citric Acid</text></g>
        <g class="note left" style="--c:var(--sour-3)" transform="rotate(408.86)"><circle r="464" pathLength="360" transform="rotate(177.43)"/><text x="-498">Tamarind</text></g>
        <g class="note left" style="--c:var(--sour-1)" transform="rotate(414)"><circle r="464" pathLength="360" transform="rotate(177.43)"/><text x="-498">Rice Vinegar</text></g>
        <g class="note left" style="--c:var(--sour-2)" transform="rotate(419.14)"><circle r="464" pathLength="360" transform="rotate(177.43)"/><text x="-498">Balsamic Vinegar</text></g>
        <g class="note left" style="--c:var(--sour-3)" transform="rotate(424.29)"><circle r="464" pathLength="360" transform="rotate(177.43)"/><text x="-498">Apple Cider Vinegar</text></g>
        <g class="note left" style="--c:var(--sour-1)" transform="rotate(429.43)"><circle r="464" pathLength="360" transform="rotate(177.43)"/><text x="-498">Sumac</text></g>
        <g class="note left" style="--c:var(--sour-2)" transform="rotate(434.57)"><circle r="464" pathLength="360" transform="rotate(177.43)"/><text x="-498">Zests</text></g>
        <g class="note left" style="--c:var(--sour-3)" transform="rotate(439.71)"><circle r="464" pathLength="360" transform="rotate(177.43)"/><text x="-498">Lime</text></g>
        <g class="note left" style="--c:var(--sour-1)" transform="rotate(444.86)"><circle r="464" pathLength="360" transform="rotate(177.43)"/><text x="-498">Lemon</text></g>
      </g>
    </g>
  </g>
</svg>
</body>
</html>
```